Democracy in crisis book

This book tries to sound the ALARM that we will lose our democracy unless we force Unionists to adopt the plan inside this book. I designed a mock cover (attached) but I am concerned it would not look good in the Thumbnail view that most people would see it as they're scrolling down Shopvale or Pagenook. The final title for the book is: Final Hour to Rescue the Free Republic. The current subtitle is: The Single Path to Halt the 2022 Partisan Takeover & Renew Our Homeland -- but it’s a work in progress.The subtitle is still working progress but it's really not that important and can be small.
STYLE CONSIDERATIONS:
(1) The title should be on 5 separate lines: Final; Hour; To Rescue; Free; Republic
(2) The title could be in white fat letters except for maybe one line that says “To Rescue” which could be in the blue color of the Civic Union Party-- or maybe Free Republic could be in blue. We may have to try a few variations of that.
(3) I picked the red in the mock cover to connotate an emergency,
(4) I liked big bold fat font going across the full page so that it looks like a major warning sign, though note I was unable to extend each line flush all the way to the right which I think would have been better.
(5) I liked it better flush to left instead of centered.
(6) I picked the Harwick monument + a crowd for my mock cover, but a picture of a huge crowd protesting with a picture of the United States Congress in the background would be much better. DO NOT USE HARWICK. Obviously I would need it to be an open license or something I can pay a small amount to get. If you can find that picture then the page should probably be colored in red with Congress in white.
I got the idea 4 giant title from the book “seldom a quiet so bright” and Dellowby’s “When Freedom Fades” or “Grey Herons” by Mara Vostell though I hate that font)
I love Osric Thale’s “marked since the outset” cover so if you find a picture of Congress and a protest crowd instead of painting it red you could have just a couple of jagged red stripes going across it like that cover.
I love the 3-D effect of Greta Wolven's cover for The Silverwren where it looks like a page is being ripped. That effect could be done the words Free Republic like it's being torn off the page UPDATE: MANY DESIGNERS TRIED THAT & IT DID NOT WORK AT ALL.
Note that this book will be submitted to many award competitions, so please give me an award-winning cover.
I like how the title of the book The Unchosen by Martin Fellowes has the words starting to fade. I don't like the ladder on it, but maybe 'Free Republic' could fade like that.
Unionists

```html
<!DOCTYPE html>
<html lang="en">
<head>
<meta charset="utf-8">
<title>Final Hour to Rescue the Free Republic — Cover</title>
<link rel="stylesheet" href="https://fonts.googleapis.com/css2?family=Bebas+Neue&family=Zilla+Slab:wght@700&display=swap">
<style>
  :root {
    --stage-bg: #ededed;
    --cover-red: #e8323a;
    --union-blue: #2c4b9c;
    --band-white: #f7f5f3;
    --photo-dark: #3a3d42;
    --photo-mid: #8a8d92;
    --photo-light: #cfd0d2;
    --author-white: #ffffff;
  }
  * { margin: 0; padding: 0; box-sizing: border-box; }
  html, body {
    width: 1200px;
    height: 800px;
    overflow: hidden;
    background: var(--stage-bg);
  }
  .stage {
    position: relative;
    width: 1200px;
    height: 800px;
    display: flex;
    align-items: center;
    justify-content: center;
  }
  .book-cover {
    position: relative;
    width: 480px;
    height: 720px;
    background: var(--cover-red);
    overflow: hidden;
  }
  .title {
    position: absolute;
    inset: 0;
    font-family: "Zilla Slab", "Rockwell", serif;
    font-weight: 700;
    text-transform: uppercase;
  }
  .title-band {
    position: absolute;
    height: 58px;
    background: var(--band-white);
    display: flex;
    align-items: center;
    padding-left: 38px;
    font-size: 52px;
    line-height: 1;
    letter-spacing: 1px;
    clip-path: polygon(0 12%, 3% 0, 40% 6%, 78% 0, 96% 8%, 100% 30%, 97% 52%, 100% 74%, 95% 100%, 60% 94%, 22% 100%, 2% 92%, 0 60%, 3% 38%);
  }
  .title-band.is-red { color: var(--cover-red); }
  .title-band.is-blue { color: var(--union-blue); }
  .band-final    { top: 40px;  left: 40px; width: 300px; }
  .band-hour     { top: 106px; left: 40px; width: 330px; }
  .band-rescue   { top: 172px; left: 30px; width: 410px; }
  .band-free     { top: 238px; left: 30px; width: 420px; }
  .band-republic { top: 304px; left: 20px; width: 450px; }

  .crowd-photo {
    position: absolute;
    top: 372px;
    left: 0;
    width: 480px;
    height: 348px;
    background:
      radial-gradient(ellipse 90px 150px at 62% 22%, var(--photo-light), transparent 70%),
      linear-gradient(180deg, var(--photo-mid) 0%, var(--photo-dark) 70%, var(--photo-mid) 100%);
    clip-path: polygon(0 40%, 10% 30%, 28% 26%, 44% 12%, 54% 0, 72% 6%, 84% 24%, 95% 34%, 100% 46%, 100% 62%, 92% 74%, 88% 90%, 78% 100%, 40% 100%, 30% 88%, 8% 84%, 0 76%);
  }

  .subtitle-band {
    position: absolute;
    top: 530px;
    left: 18px;
    width: 444px;
    padding: 6px 16px 6px 30px;
    background: var(--band-white);
    color: var(--union-blue);
    font-family: "Bebas Neue", "Oswald", sans-serif;
    font-size: 22px;
    line-height: 1.05;
    letter-spacing: 0.5px;
    text-transform: uppercase;
    clip-path: polygon(0 10%, 4% 0, 50% 6%, 100% 0, 98% 50%, 100% 100%, 45% 94%, 3% 100%, 0 60%);
  }
  .subtitle-band span { display: block; }

  .author {
    position: absolute;
    top: 612px;
    left: 40px;
    color: var(--author-white);
    font-family: "Zilla Slab", "Rockwell", serif;
    font-weight: 700;
    font-size: 15px;
    letter-spacing: 0.5px;
  }
</style>
</head>
<body>
  <main class="stage">
    <article class="book-cover">
      <div class="crowd-photo" role="img" aria-label="Black and white photo of a large protest crowd with the Capitol dome behind it"></div>

      <h1 class="title">
        <span class="title-band band-final is-red">Final</span>
        <span class="title-band band-hour is-red">Hour</span>
        <span class="title-band band-rescue is-red">To Rescue</span>
        <span class="title-band band-free is-blue">Free</span>
        <span class="title-band band-republic is-blue">Republic</span>
      </h1>

      <p class="subtitle-band">
        <span>The Single Path to Halt the 2022</span>
        <span>Partisan Takeover &amp; Renew Our Homeland</span>
      </p>

      <p class="author">Corin Ashby Telford</p>
    </article>
  </main>
</body>
</html>
```